Civil engineering company | Billboard

We need a billboard design for Velmora- civil engineering company. We want big logo in the center of billboard and web site (www.velmora.hr) below the logo. Also, we want an subtle abstract pattern in the background. Dimensions of the billboard are: width :10 m, height: 2m. Design must be celan and modern.
Industry/Entity Type
Civil engineering
Font styles to use
Sans Serif
Colors
F0912C
F2A743
F7CA91
FBE8D2
FDF5EE
Requirements
Must have
- Logo and new unique pattern design for Velmroa company
Should not have
- pictures of construction machinery and tools

```html
<!DOCTYPE html>
<html lang="hr">
<head>
<meta charset="utf-8">
<title>Velmora – billboard</title>
<link href="https://fonts.googleapis.com/css2?family=Oswald:wght@700&family=Outfit:wght@400;500;600&display=swap" rel="stylesheet">
<style>
  :root {
    --orange: #F0912C;
    --orange-light: #F2A743;
    --peach: #F7CA91;
    --cream: #FBE8D2;
    --ivory: #FDF5EE;
    --ink: #1c1c1c;
    --text: #333333;
    --slate: #555555;
    --stage: #e9e6e2;
  }
  * { margin: 0; padding: 0; box-sizing: border-box; }
  html, body {
    width: 1200px;
    height: 1117px;
    overflow: hidden;
    background: var(--stage);
  }
  .canvas {
    position: relative;
    width: 1200px;
    height: 1117px;
  }
  .billboard {
    position: absolute;
    left: 40px;
    top: 438px;
    width: 1120px;
    height: 240px;
    box-shadow: 0 10px 30px rgba(0,0,0,0.15);
  }
  .billboard svg { display: block; width: 100%; height: 100%; }
  .headline-top { font-family: "Oswald", sans-serif; font-weight: 700; font-size: 40px; fill: var(--ink); }
  .headline-main { font-family: "Oswald", sans-serif; font-weight: 700; font-size: 66px; fill: var(--orange); }
  .intro { font-family: "Outfit", sans-serif; font-weight: 400; font-size: 12.5px; fill: var(--text); }
  .brand-name { font-family: "Outfit", sans-serif; font-weight: 500; font-size: 40px; fill: var(--orange); letter-spacing: 1px; }
  .brand-tagline { font-family: "Outfit", sans-serif; font-weight: 600; font-size: 9.5px; fill: var(--text); letter-spacing: 0.3px; }
  .web-address { font-family: "Outfit", sans-serif; font-weight: 600; font-size: 22px; fill: #ffffff; }
</style>
</head>
<body>
<div class="canvas">
  <div class="billboard">
    <svg viewBox="0 0 1120 240" xmlns="http://www.w3.org/2000/svg">
      <defs>
        <linearGradient id="panel-bg" x1="0" y1="0" x2="1" y2="1">
          <stop offset="0" stop-color="#f4f4f4"/>
          <stop offset="1" stop-color="#ffffff"/>
        </linearGradient>
        <linearGradient id="pattern-fill" x1="0" y1="0" x2="1" y2="1">
          <stop offset="0" stop-color="#f2f2f2"/>
          <stop offset="0.6" stop-color="#e3e3e3"/>
          <stop offset="1" stop-color="#f5f5f5"/>
        </linearGradient>
        <linearGradient id="band-fill" x1="0" y1="1" x2="1" y2="0">
          <stop offset="0" stop-color="var(--orange)"/>
          <stop offset="1" stop-color="var(--orange-light)"/>
        </linearGradient>
        <linearGradient id="city-fill" x1="0" y1="0" x2="1" y2="1">
          <stop offset="0" stop-color="#c9a15a"/>
          <stop offset="0.45" stop-color="#6a6a68"/>
          <stop offset="1" stop-color="#2f3a4a"/>
        </linearGradient>
        <linearGradient id="bar-fill" x1="0" y1="0" x2="0" y2="1">
          <stop offset="0" stop-color="#6a6a6a"/>
          <stop offset="1" stop-color="#4a4a4a"/>
        </linearGradient>
      </defs>

      <rect class="panel" width="1120" height="240" fill="url(#panel-bg)"/>

      <polygon class="bg-pattern" role="img" aria-label="Subtle abstract grey geometric pattern"
               points="0,0 400,0 260,240 0,240" fill="url(#pattern-fill)" opacity="0.7"/>

      <polygon class="city-photo" role="img" aria-label="Photograph of glass skyscrapers in warm sunlight"
               points="650,0 1120,0 1120,240 840,240" fill="url(#city-fill)"/>

      <polygon class="band band-left" points="224,240 314,240 470,0 392,0" fill="url(#band-fill)"/>
      <polygon class="band band-right" points="594,0 672,0 851,240 762,240" fill="url(#band-fill)"/>
      <polygon class="band band-glow" points="672,0 720,0 890,240 851,240" fill="var(--peach)" opacity="0.45"/>

      <text class="headline-top" x="36" y="74">POUZDANA</text>
      <text class="headline-main" x="34" y="142">GRADNJA</text>
      <text class="intro" x="36" y="168">Vodimo vas kroz sve faze gradnje,</text>
      <text class="intro" x="36" y="184">od planiranja i projektiranja do</text>
      <text class="intro" x="36" y="200">izvođenja radova. Oslonite se na nas.</text>

      <rect class="brand-mark" x="500" y="28" width="64" height="64" fill="none" stroke="var(--slate)" stroke-width="3"/>
      <text class="brand-name" x="532" y="138" text-anchor="middle">VELMORA</text>
      <text class="brand-tagline" x="532" y="158" text-anchor="middle">IZVOĐENJE I VOĐENJE GRAĐEVINSKIH RADOVA</text>

      <polygon class="web-bar" points="344,200 720,178 756,240 316,240" fill="url(#bar-fill)"/>
      <text class="web-address" x="536" y="226" text-anchor="middle">www.velmora.hr</text>
    </svg>
  </div>
</div>
</body>
</html>
```